WinterCommuters

First, let me apologize for the short term. We just got an opportunity to place an ad in a commuter newspaper that will run throughout the winter months. We have tropical vacation rentals in Mexico, so it seems worth a shot.

We want to emphasize tropical luxury at competitive prices. Because we will be new to the audience, we need to cover a lot in one ad - images can definitely help. We are supplying photographs - feel free to crop or whatever.

We have the only private complex of luxury houses on the Mexican Caribbean coast, the "Riviera Maya" so we can accommodate anywhere from a single couple to a full wedding party. We want to show our large capacity without scaring off the single couple or small family with mom, dad, and a couple of kids.
Updates

Correction to text:  third paragraph.  The word should be "you", not "so" after "Riviera Maya,"
"As we are in the heart of the Riviera Maya, you will have "

Target Market(s)

Professionals looking to get out of the winter cold. Think tropical!

Industry/Entity Type

Wedding

Requirements
Must have
• The ad must be 5"x5" at 200 DPI (1,000 x 1000 pixels).
• The primary ad will be printed in black and white so it should be saved as a grayscale image. (I think they actually want a jpg, although a tiff would seem more logical!)
• The add will also be on the web in full color so please design the ad with color in mind and then change to grayscale after the content ends.
• Include our logo, phone number, e-mail, and website.
• Also, unless there is a good reason not to, include the four "first tier" images.
• Use the text as provided - not that some is optional.
Nice to have
• Please see the text in the attachments. OOPS: I downloaded the wrong version first - use the most recent "chicagoad" text!
• Also, unless there is a strong reason, use the "first tier" photos. We want to emphasize the accommodations, but also show large groups. We don't want to scare off the smaller groups (couples, small families) with the impression that we are only for large groups.
• The "second tier" photos are available if they would help. Both accommodation and weddings/large groups.
Should not have
• Stock photographs.
• I have (obviously) had some issues loading my files so please forgive the duplicates.

```html
<!DOCTYPE html>
<html lang="en">
<head>
<meta charset="utf-8">
<title>Villa Solana – Winter Getaway Ad</title>
<link rel="stylesheet" href="https://fonts.googleapis.com/css2?family=Archivo+Narrow:wght@400;500;700&family=Arimo:wght@400&family=Kalam:wght@400&display=swap">
<style>
  :root{
    --sky:#e4eefa;
    --lime:#bfe62a;
    --navy:#0f2a4a;
    --ink:#141414;
    --slate:#5672a6;
    --white:#ffffff;
    --pool-a:#5fb3d8; --pool-b:#2f7ea3; --pool-c:#c7b79a;
    --sunset-a:#f5a43a; --sunset-b:#e8c889; --sunset-c:#3b2a22;
    --stone-a:#9fc0e0; --stone-b:#b9a98c; --stone-c:#5c6a3a;
    --garden-a:#7fa6c9; --garden-b:#6f8f47; --garden-c:#e8e2d6;
    --room-a:#8b7a68; --room-b:#d8c7aa;
    --flower-a:#d86a8a; --flower-b:#5e8a3c;
  }
  html,body{margin:0;padding:0;width:1200px;height:1164px;overflow:hidden;background:var(--sky);}
  .ad{position:relative;width:1000px;height:970px;transform:scale(1.2);transform-origin:0 0;background:var(--sky);overflow:hidden;}

  .photo{position:absolute;border:4px solid var(--white);box-sizing:border-box;}
  .photo--pool{left:22px;top:4px;width:268px;height:198px;background:linear-gradient(180deg,var(--pool-a) 0%,#9fd3ea 45%,var(--pool-b) 60%,var(--pool-c) 100%);}
  .photo--bride{left:292px;top:2px;width:200px;height:410px;background:linear-gradient(180deg,var(--sunset-a) 0%,var(--sunset-b) 55%,var(--sunset-c) 100%);}
  .photo--villa{left:22px;top:203px;width:318px;height:220px;background:linear-gradient(180deg,var(--stone-a) 0%,var(--stone-b) 50%,var(--stone-c) 100%);}
  .photo--wedding{left:188px;top:355px;width:162px;height:150px;background:linear-gradient(180deg,var(--garden-a) 0%,var(--garden-b) 55%,var(--garden-c) 100%);}
  .photo--suite{left:22px;top:423px;width:190px;height:198px;background:linear-gradient(180deg,var(--room-a) 0%,var(--room-b) 100%);}
  .photo--courtyard{left:212px;top:505px;width:92px;height:116px;background:linear-gradient(180deg,#a98c6a 0%,var(--flower-b) 100%);}
  .photo--blooms{left:346px;top:418px;width:48px;height:54px;background:linear-gradient(135deg,var(--flower-a),var(--flower-b));}

  .questions{position:absolute;left:508px;top:2px;width:480px;margin:0;padding:0;list-style:none;
    font-family:"Kalam",cursive;font-size:22px;line-height:25.5px;color:var(--navy);}
  .questions li{position:relative;padding-left:40px;}
  .questions li::before{content:"•";position:absolute;left:2px;top:0;font-family:"Arimo",sans-serif;font-size:16px;}

  .swoosh{position:absolute;left:0;top:0;width:1000px;height:970px;}
  .swoosh text{font-family:"Archivo Narrow",sans-serif;}
  .band-lime{fill:var(--lime);}
  .band-navy{fill:var(--navy);}
  .txt-services{fill:var(--navy);font-size:64px;font-weight:500;}
  .txt-question{fill:var(--white);font-size:52px;font-weight:500;}
  .txt-url{fill:var(--navy);font-size:92px;font-weight:700;}

  .pitch{position:absolute;left:0;top:0;width:1000px;height:820px;font-family:"Arimo",sans-serif;font-size:17.5px;color:var(--ink);white-space:nowrap;}
  .pitch span{position:absolute;}

  .contact-bar{position:absolute;left:0;top:822px;width:1000px;height:148px;background:var(--slate);color:var(--white);}
  .contact-bar__phone{position:absolute;left:104px;top:54px;font-family:"Archivo Narrow",sans-serif;font-weight:700;font-size:64px;line-height:1;letter-spacing:-1px;white-space:nowrap;}
  .contact-bar__details{position:absolute;left:468px;top:26px;width:410px;font-family:"Arimo",sans-serif;font-size:15.5px;line-height:19.5px;white-space:nowrap;}
  .contact-bar__details p{margin:0;}
  .contact-bar__details .names{margin-bottom:12px;}
  .brand{position:absolute;left:880px;top:24px;width:100px;text-align:center;}
  .brand__dot{width:58px;height:58px;border-radius:50%;background:var(--white);margin:0 auto 8px;}
  .brand__name{font-family:"Arimo",sans-serif;font-size:14px;color:var(--white);}
</style>
</head>
<body>
<div class="ad">

  <div class="photo photo--pool" role="img" aria-label="Infinity pool with palm trees under a blue sky"></div>
  <div class="photo photo--villa" role="img" aria-label="Stone villa with a tower among palm trees"></div>
  <div class="photo photo--bride" role="img" aria-label="Bride in a white gown holding a bouquet at sunset"></div>
  <div class="photo photo--wedding" role="img" aria-label="Outdoor wedding ceremony with guests by the sea"></div>
  <div class="photo photo--blooms" role="img" aria-label="Tropical flowers"></div>
  <div class="photo photo--suite" role="img" aria-label="Bedroom suite with a large bed"></div>
  <div class="photo photo--courtyard" role="img" aria-label="Garden courtyard with flowering plants"></div>

  <ul class="questions">
    <li>Are you a couple looking for that<br>perfect, secluded getaway?</li>
    <li>Are you looking for a vacation in a<br>quiet, safe, family-friendly area?</li>
    <li>Are you looking to all be together for<br>a wedding, family reunion, or<br>retreat?</li>
  </ul>

  <svg class="swoosh" viewBox="0 0 1000 970">
    <path class="band-lime" d="M0 975 L0 860 C60 560 300 250 1000 180 L1000 516 Q750 532 555 598 Q420 665 290 735 Q230 820 120 975 Z"/>
    <path class="band-navy" d="M30 975 C65 770 140 645 260 560 C430 430 720 330 1000 285 L1000 415 C800 435 560 500 442 560 C330 617 180 700 118 778 C95 830 85 900 82 975 Z"/>
    <defs>
      <path id="path-services" d="M60 812 C85 640 400 330 985 262"/>
      <path id="path-question" d="M98 808 C195 640 460 460 985 365"/>
      <path id="path-url" d="M200 808 C310 680 560 550 985 490"/>
    </defs>
    <text class="txt-services"><textPath href="#path-services" textLength="1090" lengthAdjust="spacingAndGlyphs">Vacations, Weddings, Reunions, Retreats</textPath></text>
    <text class="txt-question"><textPath href="#path-question" textLength="985" lengthAdjust="spacingAndGlyphs">Wouldn't you rather be in a TROPICAL paradise?</textPath></text>
    <text class="txt-url"><textPath href="#path-url" textLength="880" lengthAdjust="spacingAndGlyphs">www.VillaSolana.com</textPath></text>
  </svg>

  <div class="pitch">
    <span style="left:900px;top:530px">Come</span>
    <span style="left:758px;top:553px">and relax in the only</span>
    <span style="left:655px;top:576px">private complex of luxury houses</span>
    <span style="left:583px;top:599px">on the beautiful Mexican Riviera.&nbsp; Only 60</span>
    <span style="left:520px;top:622px">miles South of Cancun, we are a world apart</span>
    <span style="left:466px;top:645px">from the noise and crowds of large hotels and party</span>
    <span style="left:418px;top:668px">towns.</span>
    <span style="left:372px;top:691px">Located in the quiet coastal village of Akumal, you get all of the</span>
    <span style="left:335px;top:714px">best amenities, great restaurants, magnificent snorkeling and diving,</span>
    <span style="left:299px;top:737px">beaches, and more in the laid back autmosphere that is so hard to find.</span>
    <span style="left:263px;top:760px">As we are in the heart of the Riviera Maya, you will have access to shopping,</span>
    <span style="left:231px;top:783px">Mayan ruins, tourist attractions, golf, sailing, diving and much more.</span>
  </div>

  <footer class="contact-bar">
    <div class="contact-bar__phone">(215) 555-0148</div>
    <div class="contact-bar__details">
      <p class="names">Daniel &amp; Nora Price ▪ info@VillaSolana.com ▪</p>
      <p>www.VillaSolana.com ▪ Visit our web site or call us<br>directly.&nbsp; We look forward to hearing from you and to<br>sharing our homes with you, your family and friends.</p>
    </div>
    <div class="brand">
      <div class="brand__dot"></div>
      <div class="brand__name">Villa Solana</div>
    </div>
  </footer>

</div>
</body>
</html>
```